MP7 (acronym stands for Mealport 7)

We are a sales and marketing start up. We sell bar and beverage dispensing equipment presently and we will add foodservice equipment to our portfolio in the coming year. We like our logo but we will consider different presentations of "MP7"

Industry/Entity Type

Marketing

```html
<!DOCTYPE html>
<html lang="en">
<head>
<meta charset="utf-8">
<title>MP7 Business Card</title>
<link href="https://fonts.googleapis.com/css2?family=Arimo:wght@400;700&display=swap" rel="stylesheet">
<style>
  :root {
    --page-bg: #efefef;
    --card-bg: #ffffff;
    --brand-orange: #f7941d;
    --brand-green: #a4ce39;
    --band-grey: #a7a9ac;
    --text-grey: #58595b;
  }
  html, body {
    margin: 0;
    padding: 0;
    width: 1200px;
    height: 1000px;
    overflow: hidden;
    background: var(--page-bg);
    font-family: "Arimo", Arial, sans-serif;
  }
  .card {
    position: absolute;
    left: 214px;
    top: 270px;
    width: 806px;
    height: 462px;
    background: var(--card-bg);
    box-shadow: 0 6px 18px rgba(0,0,0,0.18);
    overflow: hidden;
  }
  .brand-name {
    position: absolute;
    left: 40px;
    top: 26px;
    margin: 0;
    font-size: 86px;
    font-weight: 700;
    letter-spacing: 10px;
    line-height: 1;
    color: var(--brand-orange);
  }
  .header-band, .footer-band {
    position: absolute;
    left: 0;
    width: 806px;
  }
  .header-band { top: 134px; height: 53px; }
  .footer-band { top: 434px; height: 28px; }
  .person {
    position: absolute;
    left: 67px;
    top: 232px;
  }
  .person-name {
    margin: 0;
    font-size: 27px;
    font-weight: 700;
    color: var(--brand-orange);
  }
  .person-role {
    margin: 8px 0 0;
    font-size: 18px;
    color: var(--text-grey);
  }
  .divider {
    position: absolute;
    left: 380px;
    top: 215px;
    width: 3px;
    height: 203px;
    background: linear-gradient(to bottom, rgba(247,148,29,0), var(--brand-orange) 30%, var(--brand-orange) 70%, rgba(247,148,29,0));
  }
  .contact-list {
    position: absolute;
    left: 406px;
    top: 234px;
    margin: 0;
    padding: 0;
    list-style: none;
  }
  .contact-item {
    display: flex;
    align-items: center;
    height: 46px;
    font-size: 18px;
    color: var(--text-grey);
  }
  .contact-icon {
    width: 24px;
    height: 24px;
    margin-right: 19px;
    fill: var(--brand-orange);
  }
</style>
</head>
<body>
  <div class="card">
    <h1 class="brand-name">MP7</h1>

    <svg class="header-band" viewBox="0 0 806 53" aria-hidden="true">
      <rect x="0" y="0" width="806" height="53" fill="var(--band-grey)"/>
      <polygon points="606,0 671,0 636,53 571,53" fill="var(--brand-green)"/>
      <polygon points="671,0 806,0 806,53 636,53" fill="var(--brand-orange)"/>
    </svg>

    <div class="person">
      <p class="person-name">Your name</p>
      <p class="person-role">Yor position</p>
    </div>

    <div class="divider"></div>

    <ul class="contact-list">
      <li class="contact-item">
        <svg class="contact-icon" viewBox="0 0 24 24" aria-hidden="true"><path d="M12 1a8 8 0 0 0-8 8c0 6 8 14 8 14s8-8 8-14a8 8 0 0 0-8-8zm0 11a3 3 0 1 1 0-6 3 3 0 0 1 0 6z"/></svg>
        your address
      </li>
      <li class="contact-item">
        <svg class="contact-icon" viewBox="0 0 24 24" aria-hidden="true"><path d="M6.6 10.8a15 15 0 0 0 6.6 6.6l2.2-2.2a1 1 0 0 1 1-.25 11.4 11.4 0 0 0 3.6.6 1 1 0 0 1 1 1V20a1 1 0 0 1-1 1A17 17 0 0 1 3 4a1 1 0 0 1 1-1h3.5a1 1 0 0 1 1 1c0 1.25.2 2.45.6 3.6a1 1 0 0 1-.25 1z"/></svg>
        123 456 789
      </li>
      <li class="contact-item">
        <svg class="contact-icon" viewBox="0 0 24 24" aria-hidden="true"><path d="M2 5h20v14H2z M3.5 6.5 12 13l8.5-6.5" fill="none" stroke="var(--brand-orange)" stroke-width="0"/><path d="M2 5h20v1.2L12 13 2 6.2z"/><path d="M2 8l10 7 10-7v11H2z"/></svg>
        yourname@domain.com
      </li>
      <li class="contact-item">
        <svg class="contact-icon" viewBox="0 0 24 24" aria-hidden="true"><g fill="none" stroke="var(--brand-orange)" stroke-width="2"><circle cx="12" cy="12" r="10"/><ellipse cx="12" cy="12" rx="4.5" ry="10"/><line x1="2" y1="12" x2="22" y2="12"/><path d="M4 7h16M4 17h16"/></g></svg>
        www.mp7.com
      </li>
    </ul>

    <svg class="footer-band" viewBox="0 0 806 28" aria-hidden="true">
      <polygon points="22,0 780,0 806,28 0,28" fill="var(--band-grey)"/>
    </svg>
  </div>
</body>
</html>
```